Training Company Needs a Web Design

We are a Training company that needs a website design completed for us. "The Harbor Loft" The website will be a 'community space' specialising in 'Change and Transformation'. It will be a 'space' where individuals can come to find out 'latest news', upcoming events and courses, chat with others and find 'tools and templates'. They will need to login as a 'Member'.

The final design needs to be professional but have a 'fun and interactive' feel and appeal to our target audience who are predominantly corporate individuals.

Target Market(s)

Corporate Individuals - they may have a Change or Project background

Industry/Entity Type

Business Consultant

Number of Pages Required

3 page

Font styles to use
Sans Serif

Requirements
Must have
• Design for 'Home Page'
• A professional and corporate 'feel' but be fun and interactive.
Nice to have
• A 'sense' of how some of the other pages may be designed or laid out.

```html
<!DOCTYPE html>
<html lang="en">
<head>
<meta charset="utf-8">
<title>The Harbor Loft</title>
<link rel="stylesheet" href="https://fonts.googleapis.com/css2?family=Raleway:wght@300;400;600;700;800&family=Open+Sans:wght@400;600;700&display=swap">
<style>
:root{
  --orange:#f0522a;
  --navy:#134b8e;
  --purple:#8a64ad;
  --teal:#3fcfb4;
  --yellow:#f6c61a;
  --sky:#1b9ad8;
  --ink:#333840;
  --muted:#7b8088;
  --line:#e3e5e8;
  --foot:#f0f1f3;
  --white:#ffffff;
}
*{box-sizing:border-box;margin:0;padding:0}
html,body{width:1200px;height:3666px;overflow:hidden}
body{position:relative;background:var(--white);font-family:"Open Sans",Arial,sans-serif;color:var(--ink)}
.abs{position:absolute}
/* header + hero */
.hero{left:0;top:0;width:1200px;height:720px;background:linear-gradient(160deg,#c9c2b7 0%,#9a8e80 40%,#d9d2c9 70%,#b7aa9d 100%)}
.hero-band{left:0;top:672px;width:1200px;height:60px}
.brand{left:74px;top:20px;display:flex;align-items:center;gap:12px;color:var(--white);font-family:"Raleway",sans-serif;font-weight:700;font-size:22px;line-height:1.05;text-transform:uppercase}
.brand-mark{width:34px;height:34px;background:var(--white);border-radius:50%}
.nav{right:68px;top:36px;display:flex;align-items:center;gap:32px;font-family:"Raleway",sans-serif;font-size:15px;color:var(--white)}
.nav .active{font-weight:700}
.btn-member{background:var(--orange);color:var(--white);padding:10px 22px;border-radius:20px;font-weight:600}
.hero-title{left:0;width:1200px;top:330px;text-align:center;color:var(--white);font-family:"Raleway",sans-serif;font-weight:700;font-size:36px}
.hero-sub{left:0;width:1200px;top:384px;text-align:center;color:var(--white);font-size:17px}
.btn-start{left:527px;top:444px;width:146px;height:36px;border-radius:18px;background:var(--yellow);color:#222;font-weight:700;font-size:15px;display:flex;align-items:center;justify-content:center}
.scroll-down{left:574px;top:660px}
/* services */
.section-title{font-family:"Raleway",sans-serif;font-weight:400;font-size:28px;color:var(--ink)}
.section-title b{font-weight:700}
.services-title{left:0;width:1200px;top:804px;text-align:center}
.service{top:887px;width:257px;height:266px;color:var(--white);text-align:center;padding-top:44px;z-index:2}
.service h3{font-family:"Raleway",sans-serif;font-weight:600;font-size:21px;margin:22px 0 14px}
.service p{font-size:13px;line-height:1.6;padding:0 26px}
.s-learn{left:61px;background:var(--orange)}
.s-connect{left:330px;background:var(--navy)}
.s-collab{left:599px;background:var(--purple)}
.s-share{left:868px;background:var(--teal)}
/* welcome */
.community{left:0;top:1100px;width:1200px;height:806px;background:linear-gradient(110deg,#6b5a4d 0%,#a99887 35%,#cfc6bb 60%,#8e9aa3 100%)}
.welcome{left:587px;top:1210px;width:562px;height:562px;border-radius:50%;background:rgba(255,255,255,.9);text-align:center;padding:128px 80px 0}
.welcome h4{font-family:"Raleway",sans-serif;font-weight:400;font-size:21px}
.welcome h2{font-family:"Raleway",sans-serif;font-weight:700;font-size:35px;margin-top:4px}
.welcome .rule{width:70px;height:3px;background:var(--orange);margin:14px auto 22px}
.welcome p{font-size:14px;line-height:1.75;color:#555}
.btn-orange{display:inline-block;margin-top:20px;background:var(--orange);color:var(--white);font-size:14px;padding:9px 32px;border-radius:18px}
/* courses */
.courses-tab{left:66px;top:1760px;width:337px;height:61px;background:var(--sky);color:var(--white);font-family:"Raleway",sans-serif;font-size:26px;padding:13px 0 0 20px}
.courses-tab b{font-weight:700}
.courses{left:66px;top:1821px;width:1068px;height:305px;background:var(--white);display:flex;gap:6px;padding:7px}
.course{width:171px;background:#f2f3f5}
.course .thumb{height:146px}
.course h5{font-weight:400;font-size:16px;margin:18px 12px 6px}
.course p{font-size:12px;color:var(--muted);line-height:1.5;margin:0 12px}
.btn-more{display:inline-block;margin:12px 0 0 12px;background:var(--white);border-radius:12px;font-size:11px;padding:4px 14px}
/* events */
.events-person{left:0;top:2176px;width:410px;height:652px;background:linear-gradient(180deg,#dfe4e8 0%,#8aa3b8 55%,#4a6e93 100%)}
.events-title{left:432px;top:2208px;z-index:2}
.events-rule{left:432px;top:2256px;width:70px;height:3px;background:var(--sky)}
.event{width:340px;z-index:2}
.event h6{font-family:"Raleway",sans-serif;font-weight:600;font-size:17px;color:var(--ink)}
.event .meta{font-size:12px;color:var(--muted);margin:10px 0 14px}
.event p{font-size:13px;line-height:1.6;color:#555}
.event .link{font-size:12px;color:var(--muted);margin-top:20px}
.btn-viewall{left:1019px;top:2737px;width:105px;height:36px;border-radius:18px;background:#eceef0;font-size:14px;display:flex;align-items:center;justify-content:center}
/* speakers */
.speakers{left:0;top:2828px;width:1200px;height:520px;background:linear-gradient(100deg,#59636e 0%,#8d969f 45%,#c9cdd1 70%,#7d8590 100%)}
.speaker-avatar{left:76px;top:2882px;width:98px;height:98px;border-radius:50%;border:4px solid var(--white);background:linear-gradient(160deg,#c9d3de,#5a7394)}
.speaker-name{left:198px;top:2898px;color:var(--white);font-family:"Raleway",sans-serif;font-weight:600;font-size:21px}
.speaker-role{left:198px;top:2932px;color:var(--white);font-size:13px}
.speaker-rule{left:198px;top:2964px;width:54px;height:3px;background:var(--sky)}
.speaker-bio{left:76px;top:2998px;width:530px;color:var(--white);font-size:13px;line-height:1.7}
.btn-sky{left:76px;top:3094px;width:128px;height:38px;border-radius:19px;background:var(--sky);color:var(--white);font-size:14px;display:flex;align-items:center;justify-content:center}
.dots{left:76px;top:3190px;display:flex;gap:6px}
.dots span{width:8px;height:8px;border-radius:50%;background:rgba(255,255,255,.6)}
.dots span:first-child{background:var(--white)}
.speakers-word{left:454px;top:3142px;color:rgba(255,255,255,.85);font-family:"Raleway",sans-serif;font-weight:300;font-size:88px;letter-spacing:2px}
.and-word{left:842px;top:3226px;color:var(--white);font-family:"Raleway",sans-serif;font-size:20px}
.webinars-word{left:640px;top:3214px;color:var(--white);font-family:"Raleway",sans-serif;font-weight:800;font-size:88px}
.to-top{left:566px;top:3322px;width:68px;height:40px;border-radius:34px 34px 0 0;background:var(--foot)}
/* footer */
.footer{left:0;top:3348px;width:1200px;height:257px;background:var(--foot)}
.f-head{font-family:"Raleway",sans-serif;font-weight:600;font-size:15px;color:var(--ink)}
.f-text{font-size:12px;line-height:1.7;color:#555}
.f-links{list-style:none;font-size:12px;line-height:1.85;color:#555;margin-top:12px}
.news-item{margin-top:14px}
.news-date{font-size:11px;color:var(--muted)}
.subscribe{left:792px;top:3426px;display:flex;gap:10px}
.subscribe .field{width:210px;height:34px;background:var(--white);border-radius:17px;font-size:12px;color:#999;padding:9px 16px}
.subscribe .go{width:112px;height:34px;border-radius:17px;background:#b9bec5;color:var(--white);font-size:12px;font-weight:700;display:flex;align-items:center;justify-content:center}
.socials{left:792px;top:3520px;display:flex;gap:8px}
.socials span{width:34px;height:34px;border-radius:50%;border:2px solid #b4b9c0}
.bottom-bar{left:0;top:3605px;width:1200px;height:61px;background:var(--white);border-top:1px solid var(--line);font-size:12px;color:#555}
.copy{left:73px;top:22px}
.legal{right:74px;top:22px}
</style>
</head>
<body>

<!-- hero -->
<div class="abs hero" role="img" aria-label="Photo of smiling colleagues meeting around a table"></div>
<svg class="abs hero-band" width="1200" height="60" viewBox="0 0 1200 60" aria-hidden="true">
  <path d="M0 10 Q600 60 1200 0 V60 H0Z" fill="#f6c61a"/>
  <path d="M0 30 Q600 70 1200 25 V60 H0Z" fill="#ffffff"/>
</svg>
<div class="abs brand"><span class="brand-mark"></span><span>The<br>Harbor Loft</span></div>
<nav class="abs nav">
  <span class="active">Home</span><span>About</span><span>Services</span><span>Courses</span><span>News</span><span>Events</span><span>Contact</span>
  <span class="btn-member">Member Login</span>
</nav>
<h1 class="abs hero-title">The Harbor Loft</h1>
<p class="abs hero-sub">A 'community' whereby an individual can go to learn, connect, collaborate and share.</p>
<div class="abs btn-start">Get Started</div>
<svg class="abs scroll-down" width="52" height="52" viewBox="0 0 52 52" aria-hidden="true">
  <circle cx="26" cy="26" r="23" fill="none" stroke="#fff" stroke-width="3"/>
  <path d="M26 14 V36 M17 28 L26 37 L35 28" fill="none" stroke="#fff" stroke-width="3"/>
</svg>

<!-- services -->
<h2 class="abs section-title services-title">Our Great <b>Services</b></h2>

<div class="abs service s-learn">
  <svg width="60" height="46" viewBox="0 0 60 46" aria-hidden="true"><rect x="8" y="3" width="44" height="30" rx="3" fill="none" stroke="#fff" stroke-width="3"/><path d="M2 40 H58" stroke="#fff" stroke-width="4"/></svg>
  <h3>Learning</h3>
  <p>Lorem ipsum dolor sitt amet, elit, sed diam nonummy nibh euismod us to ins consequat.</p>
</div>
<div class="abs service s-connect">
  <svg width="60" height="46" viewBox="0 0 60 46" aria-hidden="true"><g stroke="#fff" stroke-width="2.5"><path d="M30 23 L12 8 M30 23 L48 8 M30 23 L12 40 M30 23 L48 40 M30 23 V2"/></g><g fill="#fff"><circle cx="30" cy="23" r="7"/><circle cx="12" cy="8" r="4"/><circle cx="48" cy="8" r="4"/><circle cx="12" cy="40" r="4"/><circle cx="48" cy="40" r="4"/><circle cx="30" cy="3" r="3"/></g></svg>
  <h3>Connecting</h3>
  <p>Lorem ipsum dolor sitt amet, elit, sed diam nonummy nibh euismod us to ins consequat.</p>
</div>
<div class="abs service s-collab">
  <svg width="60" height="46" viewBox="0 0 60 46" aria-hidden="true"><path d="M4 4 H36 V26 H16 L8 34 V26 H4Z" fill="#fff"/><path d="M40 14 H56 V34 H52 V42 L44 34 H24 V30 H40Z" fill="#fff"/></svg>
  <h3>Collaborating</h3>
  <p>Lorem ipsum dolor sitt amet, elit, sed diam nonummy nibh euismod us to ins consequat.</p>
</div>
<div class="abs service s-share">
  <svg width="60" height="46" viewBox="0 0 60 46" aria-hidden="true"><path d="M40 8 L18 23 L40 38" fill="none" stroke="#fff" stroke-width="3"/><g fill="#fff"><circle cx="42" cy="8" r="7"/><circle cx="17" cy="23" r="7"/><circle cx="42" cy="38" r="7"/></g></svg>
  <h3>Sharing</h3>
  <p>Lorem ipsum dolor sitt amet, elit, sed diam nonummy nibh euismod us to ins consequat.</p>
</div>

<!-- welcome -->
<div class="abs community" role="img" aria-label="Photo of a group discussion seated in a circle"></div>
<div class="abs welcome">
  <h4>Welcome to</h4>
  <h2>The Harbor Loft</h2>
  <div class="rule"></div>
  <p>Lorem ipsum dolor sit amet, consectetuer adipiscing elit, sed diam nonummy nibh euismod tincidunt ut laoreet dolore magna aliquam erat volutpat. Ut wisi enim ad minim veniam, quis nostrud exerci tation ullamcorper suscipit lobortis nisl ut aliquip ex ea commodo consequat.</p>
  <span class="btn-orange">Learn More</span>
</div>

<!-- courses -->
<div class="abs courses-tab">Upcoming <b>Courses</b></div>
<div class="abs courses">
  <div class="course"><div class="thumb" role="img" aria-label="Paint brushes" style="background:linear-gradient(135deg,#d8c2a0,#5d4a3a)"></div><h5>Art</h5><p>Imperdiet doming id tationem lectorum.</p><span class="btn-more">More</span></div>
  <div class="course"><div class="thumb" role="img" aria-label="Photographer with camera" style="background:linear-gradient(135deg,#b7c79a,#3d4a3a)"></div><h5>Photography</h5><p>Imperdiet doming id tationem lectorum.</p><span class="btn-more">More</span></div>
  <div class="course"><div class="thumb" role="img" aria-label="Screens showing websites" style="background:linear-gradient(135deg,#e4ecf3,#6d8fb1)"></div><h5>Web design</h5><p>Imperdiet doming id tationem lectorum.</p><span class="btn-more">More</span></div>
  <div class="course"><div class="thumb" role="img" aria-label="Runner on a trail" style="background:linear-gradient(135deg,#9fb2c4,#b08a5e)"></div><h5>Health &amp; Fitness</h5><p>Imperdiet doming id tationem lectorum.</p><span class="btn-more">More</span></div>
  <div class="course"><div class="thumb" role="img" aria-label="Hands with financial charts" style="background:linear-gradient(135deg,#c3ccd4,#55616d)"></div><h5>Financial</h5><p>Imperdiet doming id tationem lectorum.</p><span class="btn-more">More</span></div>
  <div class="course"><div class="thumb" role="img" aria-label="Piano keys" style="background:linear-gradient(135deg,#8a7a70,#2a2426)"></div><h5>Music</h5><p>Imperdiet doming id tationem lectorum.</p><span class="btn-more">More</span></div>
</div>

<!-- events -->
<div class="abs events-person" role="img" aria-label="Photo of a man holding a tablet"></div>
<h2 class="abs section-title events-title">Upcoming <b>Events</b></h2>
<div class="abs events-rule"></div>

<div class="abs event" style="left:432px;top:2320px">
  <h6>Lorem ipsum dolor sit amet</h6><div class="meta">03 March 2016 &nbsp;|&nbsp; London</div>
  <p>Lorem ipsum dolor sit amet, consectetuer adipiscing elit, sed diam nonummy nibh euismod tincidunt ut quod mazim placerat facer possim assum.</p>
  <div class="link">Learn More &rarr;</div>
</div>
<div class="abs event" style="left:792px;top:2320px">
  <h6>Lorem ipsum dolor sit amet</h6><div class="meta">03 March 2016 &nbsp;|&nbsp; USA</div>
  <p>Lorem ipsum dolor sit amet, consectetuer adipiscing elit, sed diam nonummy nibh euismod tincidunt ut quod mazim placerat facer possim assum.</p>
  <div class="link">Learn More &rarr;</div>
</div>
<div class="abs event" style="left:432px;top:2532px">
  <h6>Lorem ipsum dolor sit amet</h6><div class="meta">03 March 2016 &nbsp;|&nbsp; Australia</div>
  <p>Lorem ipsum dolor sit amet, consectetuer adipiscing elit, sed diam nonummy nibh euismod tincidunt ut quod mazim placerat facer possim assum.</p>
  <div class="link">Learn More &rarr;</div>
</div>
<div class="abs event" style="left:792px;top:2532px">
  <h6>Lorem ipsum dolor sit amet</h6><div class="meta">03 March 2016 &nbsp;|&nbsp; United Kingdom</div>
  <p>Lorem ipsum dolor sit amet, consectetuer adipiscing elit, sed diam nonummy nibh euismod tincidunt ut quod mazim placerat facer possim assum.</p>
  <div class="link">Learn More &rarr;</div>
</div>
<div class="abs btn-viewall">View All</div>

<!-- speakers -->
<div class="abs speakers" role="img" aria-label="Photo of a woman speaking at a microphone"></div>
<div class="abs speaker-avatar" role="img" aria-label="Speaker portrait"></div>
<div class="abs speaker-name">Daniel Morrow</div>
<div class="abs speaker-role">Lorem ipsum dolor sit amet, elit, ...</div>
<div class="abs speaker-rule"></div>
<p class="abs speaker-bio">Lorem ipsum dolor sit amet, consectetuer adipiscing elit, sed diam nonummy nibh euismod tincidunt ut laoreet dolore magna aliquam erat soluta nobis eleifend option congue nihil imperdiet doming id quod mazim placerat facer possim assum.</p>
<div class="abs btn-sky">Learn More</div>
<div class="abs dots"><span></span><span></span><span></span><span></span><span></span></div>
<div class="abs speakers-word">SPEAKERS</div>
<div class="abs and-word">and</div>
<div class="abs webinars-word">WEBINARS</div>

<!-- footer -->
<div class="abs footer"></div>
<div class="abs to-top"><svg width="68" height="40" viewBox="0 0 68 40" aria-hidden="true"><circle cx="34" cy="24" r="11" fill="none" stroke="#999" stroke-width="2"/><path d="M29 27 L34 21 L39 27" fill="none" stroke="#999" stroke-width="2"/></svg></div>

<div class="abs" style="left:73px;top:3382px;width:310px">
  <div class="f-head">Latest News</div>
  <div class="news-item"><div class="news-date">03 March 2016</div><p class="f-text">Lorem ipsum dolor sit amet, consectetuer adipiscing elit, sed diam nonummy nibh euismod tincidunt ut quod mazim placerat facer possim assum.</p></div>
  <div class="news-item" style="margin-top:24px"><div class="news-date">03 March 2016</div><p class="f-text">Lorem ipsum dolor sit amet, consectetuer adipiscing elit, sed diam nonummy nibh euismod tincidunt ut quod mazim placerat facer possim assum.</p></div>
</div>
<div class="abs" style="left:432px;top:3382px">
  <div class="f-head">Quick Links</div>
  <ul class="f-links"><li>Home</li><li>About</li><li>Services</li><li>Courses</li><li>News</li><li>Events</li><li>Contact</li></ul>
</div>
<div class="abs" style="left:584px;top:3382px;width:200px">
  <div class="f-head">Contact Info</div>
  <p class="f-text" style="margin-top:12px">14 Quay Lane,<br>Harbor District - 400112</p>
  <p class="f-text" style="margin-top:8px">1800 555 014<br>hello@harborloft.example</p>
  <p class="f-text" style="margin-top:8px">Website:<br>harborloft.example</p>
</div>
<div class="abs f-head" style="left:792px;top:3382px">Subscribe Our Newsletter!</div>
<div class="abs subscribe"><div class="field">Email Address</div><div class="go">SUBSCRIBE</div></div>
<div class="abs f-head" style="left:792px;top:3486px">Stay Connected</div>
<div class="abs socials"><span></span><span></span><span></span><span></span><span></span><span></span></div>

<div class="abs bottom-bar">
  <div class="abs copy">Copyright &copy; 2016 The Harbor Loft. All Rights Reserved</div>
  <div class="abs legal">Privacy Policy &nbsp;|&nbsp; Terms Of Use &nbsp;|&nbsp; Sitemap</div>
</div>

</body>
</html>
```